Clean business card with logo provided

I want a card that will stand out among the masses. I need the color and image to show professionalism and yet have a family appeal showing that I only deal with win/win scenarios. The back of the card will be used to take notes about the individual so I can use that in my database entry. I like modern design but need professionalism in it also. It needs to fit my "clean, safe, and affordable housing" motto. I need to be able to write on the file and update the card details for my employees.

Target Market(s)

Investors looking to make investment income through real estate

Industry/Entity Type

Real Estate

Contact Information for Business Card

Troy Vandemark
blank address, city, st, zip code
480-555-0147
troyvandemark@quillrentals.example
www.quillrentals.example

Font styles to use
Sans Serif

Requirements
Must have
• I would like the back of the card to have lines for info. example
• Met/Visited: Date:
• Interets:
Nice to have
• I want the cards color to match the logo background color. Font with details to be san serif and black. I want the card rectangular with square corners. Standard business card size. I would like to see cards designed with both images to see which i prefer more.

```html
<!DOCTYPE html>
<html lang="en">
<head>
<meta charset="utf-8">
<title>Quill Rentals LLC – Business Card</title>
<link rel="stylesheet" href="https://fonts.googleapis.com/css2?family=Montserrat:wght@400;500;700&display=swap">
<style>
  :root {
    --card-teal: #17b6cf;
    --frame-teal: #00abc8;
    --back-paper: #f2f2f4;
    --ink: #111111;
    --white: #ffffff;
    --page: #ffffff;
  }
  html, body {
    margin: 0;
    padding: 0;
    width: 1199px;
    height: 1200px;
    overflow: hidden;
    background: var(--page);
    font-family: "Montserrat", sans-serif;
  }
  .canvas {
    position: relative;
    width: 1199px;
    height: 1200px;
  }
  .card {
    position: absolute;
    left: 267px;
    width: 644px;
    height: 366px;
    box-sizing: border-box;
  }
  .card-front {
    top: 188px;
    background: var(--card-teal);
  }
  .brand {
    position: absolute;
    left: 32px;
    top: 58px;
    display: flex;
    align-items: center;
    gap: 12px;
  }
  .brand-mark {
    width: 30px;
    height: 30px;
    border-radius: 50%;
    background: var(--ink);
  }
  .brand-name {
    color: var(--white);
    font-weight: 500;
    font-size: 30px;
    letter-spacing: 3px;
    line-height: 1;
  }
  .tagline {
    position: absolute;
    left: 42px;
    top: 130px;
    margin: 0;
    color: var(--white);
    font-size: 10.5px;
    font-weight: 400;
    letter-spacing: 0.2px;
  }
  .holder {
    position: absolute;
    left: 277px;
    top: 200px;
  }
  .holder-name {
    margin: 0 0 20px;
    color: var(--white);
    font-size: 29px;
    font-weight: 700;
    letter-spacing: 3.2px;
    line-height: 1;
  }
  .contact {
    list-style: none;
    margin: 0;
    padding: 0;
    color: var(--ink);
    font-size: 13.6px;
    font-weight: 400;
    letter-spacing: 1px;
    line-height: 23.5px;
  }
  .contact .web { margin-left: 10px; }

  .card-back {
    top: 656px;
    background: var(--back-paper);
  }
  .notes-frame {
    position: absolute;
    left: 31px;
    top: 30px;
    width: 582px;
    height: 306px;
    box-sizing: border-box;
    border: 21px solid var(--frame-teal);
    background: var(--back-paper);
  }
  .note-row {
    position: absolute;
    left: 25px;
    right: 23px;
    display: flex;
    align-items: baseline;
    gap: 24px;
  }
  .note-label {
    font-size: 20.5px;
    font-weight: 700;
    letter-spacing: 2.6px;
    color: var(--ink);
    white-space: nowrap;
  }
  .note-line {
    flex: 1;
    border-bottom: 1.6px dotted #555;
    transform: translateY(-2px);
  }
  .row-met { top: 30px; }
  .row-interest { top: 93px; }
  .row-problems { top: 156px; }
  .row-date { top: 219px; }
</style>
</head>
<body>
<main class="canvas">
  <section class="card card-front" aria-label="Business card front">
    <div class="brand">
      <span class="brand-mark"></span>
      <span class="brand-name">QUILL RENTALS LLC</span>
    </div>
    <p class="tagline">Providing clean, safe, and affordable housing</p>
    <div class="holder">
      <h1 class="holder-name">TROY VANDEMARK</h1>
      <ul class="contact">
        <li>TROYVANDEMARK@QUILLRENTALS.EXAMPLE</li>
        <li>BLANK ADDRESS, CITY, ST, ZIP CODE</li>
        <li>480.555.0147<span class="web">WWW.QUILLRENTALS.EXAMPLE</span></li>
      </ul>
    </div>
  </section>

  <section class="card card-back" aria-label="Business card back, notes">
    <div class="notes-frame">
      <div class="note-row row-met"><span class="note-label">MET/VISITED</span><span class="note-line"></span></div>
      <div class="note-row row-interest"><span class="note-label">INTEREST</span><span class="note-line"></span></div>
      <div class="note-row row-problems"><span class="note-label">PROBLEMS</span><span class="note-line"></span></div>
      <div class="note-row row-date"><span class="note-label">DATE</span><span class="note-line"></span></div>
    </div>
  </section>
</main>
</body>
</html>
```